Stainless Steel Letter Box plate

I need to have a letter box plate front in stainless steel that I what to have designed.

I have attached the Design of the brick letter box that has already been made.

The dimensions of the brick are set and the hole for the letters is in a set location. ( Give or take small amount )

The stainless steel manufacturer has sent a draft of the front of the plate that I thought was a bit boring and plain ( Attached )

The Stainless plate is to go on the front of the Letter box and wrap around to the left side. Brick and render will be ( is to be ) shown on the top and bottom margins of the stainless steel plate

Remember it needs to be cut out of Stainless Steel so that the number 4 needs to have joins.

The Stainless will go on the Front of the letter box and wrap around the left hand side of the letter box.

Industry/Entity Type

Steel

Requirements
Must have
• Letter Drop needs to be in set location
• Number 4
• Mirov or Mirov Rd

```html
<!DOCTYPE html>
<html lang="en">
<head>
<meta charset="utf-8">
<title>Mirov Rd Letter Box Plate</title>
<link rel="stylesheet" href="https://fonts.googleapis.com/css2?family=Yellowtail&display=block">
<style>
  :root {
    --page-bg: #ffffff;
    --plate-steel: #bcbdc0;
    --ink-dark: #414042;
  }
  * { margin: 0; padding: 0; box-sizing: border-box; }
  html, body {
    width: 1200px;
    height: 675px;
    overflow: hidden;
    background: var(--page-bg);
  }
  .canvas {
    position: relative;
    width: 1200px;
    height: 675px;
    background: var(--page-bg);
  }
  .plate {
    position: absolute;
    left: 150px;
    top: 214px;
    width: 900px;
    height: 248px;
    background: var(--plate-steel);
  }
  .letter-slot {
    position: absolute;
    left: 42px;
    top: 41px;
    width: 228px;
    height: 34px;
    background: var(--ink-dark);
  }
  .street-name {
    position: absolute;
    left: 40px;
    top: 84px;
    font-family: "Yellowtail", "Brush Script MT", "Segoe Script", "Lucida Handwriting", cursive;
    font-size: 124px;
    font-weight: 400;
    line-height: 1;
    color: var(--ink-dark);
    white-space: nowrap;
    letter-spacing: -1px;
  }
  .house-number {
    position: absolute;
    left: 696px;
    top: 36px;
    width: 140px;
    height: 160px;
    overflow: visible;
  }
  .house-number path,
  .house-number circle {
    stroke: var(--ink-dark);
    fill: none;
    stroke-linecap: round;
    stroke-linejoin: round;
  }
  .house-number .stem-cap { fill: var(--ink-dark); stroke: none; }
</style>
</head>
<body>
  <main class="canvas">
    <section class="plate" aria-label="Letter box plate">
      <div class="letter-slot" aria-hidden="true"></div>
      <p class="street-name">Mirov Rd</p>
      <svg class="house-number" viewBox="0 0 140 160" role="img" aria-label="4">
        <path class="diagonal" d="M14 114 C40 86, 70 52, 100 24" stroke-width="11"/>
        <path class="stem" d="M124 18 C120 60, 98 108, 86 148" stroke-width="19"/>
        <circle class="stem-cap" cx="122" cy="14" r="11"/>
        <path class="crossbar" d="M10 120 Q62 108 128 110" stroke-width="10"/>
      </svg>
    </section>
  </main>
</body>
</html>
```